New Business Card Design Project

Would like you to take my logo and create a business card much like the Bramblecove leasing.
I can get you the fonts used for the back of the card.
I want the same speckled blue with my logo on it.

Feel free to improve upon the balloon part of the logo if you can.
I put one I was doing with a new balloon and a more "string-like" "I".

```html
<!DOCTYPE html>
<html lang="en">
<head>
<meta charset="utf-8">
<title>Bramblecove Leasing – Business Card</title>
<link rel="stylesheet" href="https://fonts.googleapis.com/css2?family=Open+Sans:wght@400;600;700&display=swap">
<style>
  :root {
    --backdrop: #4a403a;
    --card: #1c1c1c;
    --card-edge: #111111;
    --ink: #f2f2f2;
    --ink-soft: #d6d6d6;
    --accent: #8cc63f;
    --emboss: #2a2a2a;
    --badge: #e8e8e8;
  }
  * { box-sizing: border-box; margin: 0; padding: 0; }
  html, body {
    width: 1200px; height: 793px; overflow: hidden;
    background: var(--backdrop);
    font-family: "Open Sans", Arial, sans-serif;
  }
  .sheet {
    position: relative; width: 1200px; height: 793px;
    display: flex; align-items: center; justify-content: center; gap: 40px;
  }
  .card {
    position: relative; width: 540px; height: 310px;
    background: var(--card);
    border: 1px solid var(--card-edge);
    box-shadow: 0 10px 24px rgba(0,0,0,.35);
    color: var(--ink);
  }
  /* back face */
  .card--back { display: flex; align-items: center; justify-content: center; }
  .brand-emboss {
    font-weight: 600; font-size: 44px; letter-spacing: 2px;
    color: var(--emboss); text-transform: uppercase; text-align: center; line-height: 1.1;
  }
  /* front face */
  .brand {
    position: absolute; left: 34px; top: 72px;
    display: flex; align-items: center; gap: 10px;
  }
  .brand__dot { width: 16px; height: 16px; border-radius: 50%; background: var(--accent); flex: none; }
  .brand__name {
    font-weight: 600; font-size: 26px; line-height: 1.15;
    color: var(--ink); text-transform: uppercase; letter-spacing: 1.5px;
  }
  .contact {
    position: absolute; left: 320px; top: 58px;
    font-size: 13px; line-height: 1.5; color: var(--ink-soft);
  }
  .contact__name { font-weight: 700; font-size: 20px; color: var(--accent); line-height: 1.1; }
  .contact__role { font-size: 12.5px; margin-bottom: 8px; }
  .contact__address { margin-bottom: 6px; }
  .contact__line { display: flex; align-items: center; gap: 6px; }
  .contact__line svg { width: 11px; height: 11px; flex: none; }
  .coupons {
    position: absolute; left: 20px; right: 20px; bottom: 22px;
    display: flex; justify-content: space-between;
  }
  .coupon { display: flex; flex-direction: column; align-items: center; gap: 6px; }
  .coupon__badge { width: 22px; height: 18px; background: var(--badge); border-radius: 2px; }
  .coupon__text { font-size: 9.5px; color: var(--ink-soft); }
</style>
</head>
<body>
<main class="sheet">
  <section class="card card--back" aria-label="Card back">
    <p class="brand-emboss">Bramblecove<br>Leasing</p>
  </section>

  <section class="card card--front" aria-label="Card front">
    <div class="brand">
      <span class="brand__dot"></span>
      <span class="brand__name">Bramblecove<br>Leasing</span>
    </div>

    <div class="contact">
      <p class="contact__name">Daniel Hartwell</p>
      <p class="contact__role">Managing Member</p>
      <p class="contact__address">2210 Meridian Lane,<br>Fairhaven, CA 95012</p>
      <p class="contact__line">
        <svg viewBox="0 0 12 12" aria-hidden="true"><path d="M2.5 1h2l1 3-1.3 1a6 6 0 0 0 2.8 2.8l1-1.3 3 1v2a1 1 0 0 1-1 1A9 9 0 0 1 1.5 2a1 1 0 0 1 1-1z" fill="var(--accent)"/></svg>
        (555) 014-2281
      </p>
      <p class="contact__line">
        <svg viewBox="0 0 12 12" aria-hidden="true"><rect x="3" y="0.5" width="6" height="11" rx="1.2" fill="var(--accent)"/><rect x="4.2" y="2" width="3.6" height="6.5" fill="var(--card)"/></svg>
        (555) 017-4390
      </p>
      <p class="contact__line">
        <svg viewBox="0 0 12 12" aria-hidden="true"><rect x="0.5" y="2" width="11" height="8" fill="var(--accent)"/><path d="M0.5 2l5.5 4.5L11.5 2" stroke="var(--card)" fill="none"/></svg>
        daniel@bramblecove.com
      </p>
      <p class="contact__line">
        <svg viewBox="0 0 12 12" aria-hidden="true"><circle cx="6" cy="6" r="5.3" fill="var(--accent)"/><path d="M0.7 6h10.6M6 0.7c-2.5 3-2.5 7.6 0 10.6M6 0.7c2.5 3 2.5 7.6 0 10.6" stroke="var(--card)" stroke-width=".8" fill="none"/></svg>
        www.bramblecoveleasing.com
      </p>
    </div>

    <div class="coupons">
      <div class="coupon"><span class="coupon__badge"></span><span class="coupon__text">$10 off any purchase over $100</span></div>
      <div class="coupon"><span class="coupon__badge"></span><span class="coupon__text">$10 off any purchase over $100</span></div>
      <div class="coupon"><span class="coupon__badge"></span><span class="coupon__text">$10 off any purchase over $100</span></div>
    </div>
  </section>
</main>
</body>
</html>
```